Packaging Artwork for "Earth's First Expanding Biodisposable Loofah Pads"

Our company manufactures BrisaPods. They are Earth's first expanding, biodisposable loofah pads for exfoliating the skin.
BrisaPods are biodisposable, so they can be thrown-away (or composted) before nasty skin bacteria can grow on them. This makes scrubbing skin cleaner and safer.
This is a high-end product, so our packaging needs to be very clean, sophisticated and make our product look like it should be expensive. The packaging should also let the viewer know the product is environmentally friendly.
The product name is "BrisaPods". The packaging also has to say "Biodisposable".
Our new packaging is a hanging bag with a window in it. See the image attached. There is also a picture of our current packaging for our Tarnivelles sponges. We would like completely different artwork, but keep the white paper.
The attached images are of our kitchen cleaning pads "Quorlimates". This new packaging is for "BrisaPods" which are a beauty product and the artwork must be different. Also, the packaging should have a large image of the round loofah pad on the front and the image of the loofah expanding from thin to thick on the back.
Updates

This will be a 4-inch x 4-inch bag that will hang from a hook. The bag will be about 2-inches thick. The logo will be similar to the Quorlimates fish logo that has been added to the project. Instead of saying "tarnivelles", the word "BrisaPods" needs to be used in the logo.

Industry/Entity Type

health and beauty

Requirements
Must have
• slogan "Clean Germ Free. Guilt Free". The product should be called "Earth's First Expanding Biodisposable Bath Loofahs". simple clean design on a white background. see the picture of our current packaging below. We will use the same paper. We just need completely different, sophisticated artwork

```html
<!DOCTYPE html>
<html lang="en">
<head>
<meta charset="utf-8">
<title>BrisaPods – Bath Loofah Pouch Front</title>
<link rel="stylesheet" href="https://fonts.googleapis.com/css2?family=Montserrat:wght@400;500;700&family=Raleway:wght@600;800&display=swap">
<style>
  :root {
    --backdrop: #ececec;
    --paper: #fbfbfb;
    --seal-line: #d9d9d9;
    --brand-ink: #4d3b3f;
    --brand-dot: #bfe3f1;
    --pink: #e899b9;
    --pink-soft: #f0b4cf;
    --teal: #167e8f;
    --water-light: #9fd0f2;
    --water-mid: #4f9fe6;
    --water-deep: #2f7fd6;
    --white: #ffffff;
  }
  * { margin: 0; padding: 0; box-sizing: border-box; }
  html, body { width: 1200px; height: 990px; overflow: hidden; background: var(--backdrop); }
  .pouch-face {
    position: absolute; left: 280px; top: 20px;
    width: 640px; height: 950px;
    background: var(--paper);
    overflow: hidden;
  }
  .seal-strip {
    position: absolute; left: 0; top: 0; width: 100%; height: 80px;
    border-bottom: 1px solid var(--seal-line);
  }
  .seal-strip::before, .seal-strip::after {
    content: ""; position: absolute; left: 0; width: 100%; height: 1px; background: var(--seal-line);
  }
  .seal-strip::before { top: 22px; }
  .seal-strip::after { top: 38px; }
  .hang-slot {
    position: absolute; left: 246px; top: 48px; width: 148px; height: 22px;
    border: 1.5px solid #cfcfcf; border-radius: 11px; background: #f4f4f4;
  }
  .brand {
    position: absolute; left: 0; top: 190px; width: 100%;
    display: flex; align-items: center; justify-content: center; gap: 18px;
  }
  .brand-dot {
    width: 64px; height: 64px; border-radius: 50%; background: var(--brand-dot);
  }
  .brand-name {
    font-family: "Montserrat", sans-serif; font-weight: 500;
    font-size: 56px; color: var(--brand-ink); letter-spacing: 0.5px;
  }
  .product-title {
    position: absolute; left: 0; top: 338px; width: 100%;
    text-align: center; font-family: "Raleway", sans-serif;
  }
  .product-title .kicker {
    display: block; font-weight: 600; font-size: 28px; color: var(--pink); letter-spacing: 0.5px;
  }
  .product-title .feature {
    display: block; font-weight: 800; font-size: 43px; color: var(--teal); line-height: 1.12; margin-top: 4px;
  }
  .product-title .category {
    display: block; font-weight: 800; font-size: 43px; color: var(--pink); line-height: 1.12;
  }
  .product-window {
    position: absolute; left: 127px; top: 488px; width: 386px; height: 258px;
    border-radius: 50%;
    background: radial-gradient(ellipse at 50% 40%, var(--pink-soft), var(--pink));
  }
  .water-band { position: absolute; left: 0; top: 700px; width: 640px; height: 250px; }
  .slogan {
    position: absolute; left: 0; top: 858px; width: 100%; text-align: center;
    font-family: "Montserrat", sans-serif; font-weight: 400; font-size: 31px;
    color: var(--white); letter-spacing: 0.3px;
  }
</style>
</head>
<body>
  <main class="pouch-face">
    <div class="seal-strip"><div class="hang-slot"></div></div>

    <div class="brand">
      <span class="brand-dot"></span>
      <span class="brand-name">BrisaPods</span>
    </div>

    <h1 class="product-title">
      <span class="kicker">EARTH'S FIRST EXPANDING</span>
      <span class="feature">BIODISPOSABLE</span>
      <span class="category">BATH LOOFAHS</span>
    </h1>

    <div class="product-window" role="img" aria-label="Round pink loofah pad seen through the bag window"></div>

    <svg class="water-band" viewBox="0 0 640 250" role="img" aria-label="Blue water with bubbles along the bottom of the bag">
      <defs>
        <linearGradient id="water-fill" x1="0" y1="0" x2="0" y2="1">
          <stop offset="0" stop-color="var(--water-deep)"/>
          <stop offset="0.45" stop-color="var(--water-mid)"/>
          <stop offset="1" stop-color="var(--water-light)"/>
        </linearGradient>
      </defs>
      <path d="M0 50 C120 20 230 70 360 45 C470 25 560 30 640 40 L640 250 L0 250 Z" fill="url(#water-fill)"/>
      <path d="M0 62 C130 35 240 82 370 58 C480 38 570 44 640 52" fill="none" stroke="#ffffff" stroke-opacity="0.45" stroke-width="2"/>
    </svg>

    <p class="slogan">Clean Germ Free. Guilt Free</p>
  </main>
</body>
</html>
```